Hal's Remedies Business Card Design Project

I need a business card designed for my pharmacy Hal's Remedies. I would like just the logo on one side, maybe with black background and white lettering. The other side I would also like to include my logo which is attached. Also, please include my name and the following information:
Hal Norwick Owner/Pharm D.
Business address is 7163 N Birch Rd Sioux Falls, SD 57291.
Phone number is 605-318-6027 and fax # is 605-318-6031.
my email address is hal@halsremedies.example.
My website is www.halsremedies.example.
My business hours are Monday-Friday 8am-7 pm. Saturday 8am-12 pm. Sunday Closed.
I would like the design to include my logo colors, black, white, and neon green. Silver may be added as a highlight. Thanks.
Pharmacy
See above in product description

```html
<!DOCTYPE html>
<html lang="en">
<head>
<meta charset="utf-8">
<title>Hal's Remedies – Business Card</title>
<link rel="stylesheet" href="https://fonts.googleapis.com/css2?family=Michroma&family=Open+Sans:ital,wght@0,400;0,600;1,400&display=swap">
<style>
  :root {
    --page-bg: #e9e9e7;
    --card-white: #ffffff;
    --card-mist: #e4e4e4;
    --charcoal: #3a3a3a;
    --ink: #2f2f2f;
    --neon-green: #8cc63f;
    --divider: #9a9a9a;
    --contact-text: #ffffff;
  }
  * { box-sizing: border-box; margin: 0; padding: 0; }
  html, body {
    width: 1200px; height: 901px; overflow: hidden;
    background: var(--page-bg);
  }
  .card {
    position: absolute; left: 240px;
    width: 720px; height: 411px;
    border-radius: 38px; overflow: hidden;
    background: linear-gradient(160deg, var(--card-white) 35%, var(--card-mist) 100%);
    box-shadow: 0 12px 28px rgba(0,0,0,0.16);
    font-family: "Open Sans", Arial, sans-serif;
  }
  .card--back { top: 26px; }
  .card--front { top: 464px; }

  .brand { display: flex; align-items: center; }
  .brand-square { background: var(--charcoal); border-radius: 4px; flex: none; }
  .brand-divider { background: var(--divider); transform: rotate(12deg); flex: none; }
  .brand-name { font-weight: 600; color: var(--ink); letter-spacing: -0.5px; white-space: nowrap; }

  .card--back .brand {
    position: absolute; inset: 0; justify-content: center; gap: 26px;
  }
  .card--back .brand-square { width: 52px; height: 52px; }
  .card--back .brand-divider { width: 2px; height: 84px; }
  .card--back .brand-name { font-size: 48px; }

  .card--front .brand { position: absolute; left: 48px; top: 38px; gap: 19px; }
  .card--front .brand-square { width: 38px; height: 38px; }
  .card--front .brand-divider { width: 2px; height: 60px; }
  .card--front .brand-name { font-size: 34px; }

  .card-shapes { position: absolute; inset: 0; width: 100%; height: 100%; }

  .holder { position: absolute; left: 48px; top: 138px; }
  .holder-name {
    font-family: "Michroma", Arial, sans-serif;
    font-size: 19px; color: var(--ink); letter-spacing: 1.5px;
  }
  .holder-title { margin-top: 4px; font-size: 15px; font-style: italic; color: var(--ink); }
  .holder-hours { margin-top: 6px; font-size: 12.5px; color: var(--ink); }

  .contact-list {
    position: absolute; right: 40px; bottom: 24px;
    list-style: none; text-align: right;
    color: var(--contact-text); font-size: 14.5px; line-height: 25px;
  }
  .contact-list li { display: flex; justify-content: flex-end; align-items: center; gap: 10px; white-space: nowrap; }
  .contact-list svg { width: 16px; height: 16px; flex: none; }
</style>
</head>
<body>
  <section class="card card--back">
    <div class="brand">
      <span class="brand-square"></span>
      <span class="brand-divider"></span>
      <span class="brand-name">Hal's Remedies</span>
    </div>
  </section>

  <main class="card card--front">
    <svg class="card-shapes" viewBox="0 0 840 480" preserveAspectRatio="none" aria-hidden="true">
      <path d="M0,292 C210,380 560,385 840,190 L840,480 L0,480 Z" fill="var(--charcoal)"/>
      <path d="M0,262 C170,350 430,372 650,322 C430,360 190,352 0,296 Z" fill="var(--neon-green)"/>
    </svg>

    <header class="brand">
      <span class="brand-square"></span>
      <span class="brand-divider"></span>
      <span class="brand-name">Hal's Remedies</span>
    </header>

    <section class="holder">
      <p class="holder-name">HAL NORWICK</p>
      <p class="holder-title">Owner / Pharm D.</p>
      <p class="holder-hours">Mon–Fri 8am–7pm · Sat 8am–12pm · Sun Closed</p>
    </section>

    <ul class="contact-list">
      <li>605-318-6027
        <svg viewBox="0 0 18 18"><path d="M4 2 L7 2 L8 6 L6 7.5 C7 10 8 11 10.5 12 L12 10 L16 11 L16 14 C16 15 15 16 14 16 C7 15.5 2.5 11 2 4 C2 3 3 2 4 2 Z" fill="#fff"/></svg>
      </li>
      <li>Fax 605-318-6031
        <svg viewBox="0 0 18 18"><rect x="5" y="1.5" width="8" height="5" fill="none" stroke="#fff" stroke-width="1.4"/><rect x="1.5" y="6.5" width="15" height="7" rx="1" fill="#fff"/><rect x="5" y="11" width="8" height="5.5" fill="#fff" stroke="var(--charcoal)" stroke-width="1"/></svg>
      </li>
      <li>hal@halsremedies.example
        <svg viewBox="0 0 18 18"><rect x="1" y="4" width="16" height="11" fill="#fff"/><path d="M1 4 L9 10.5 L17 4" fill="none" stroke="var(--charcoal)" stroke-width="1.3"/></svg>
      </li>
      <li>www.halsremedies.example
        <svg viewBox="0 0 18 18" fill="none" stroke="#fff" stroke-width="1.3"><circle cx="9" cy="9" r="7.5"/><ellipse cx="9" cy="9" rx="3.3" ry="7.5"/><path d="M1.5 9 H16.5 M3 5 H15 M3 13 H15"/></svg>
      </li>
      <li>7163 N Birch Rd Sioux Falls, SD 57291
        <svg viewBox="0 0 18 18"><path d="M9 17 C9 17 3 10.5 3 7 A6 6 0 0 1 15 7 C15 10.5 9 17 9 17 Z" fill="#fff"/><circle cx="9" cy="7" r="2.2" fill="var(--charcoal)"/></svg>
      </li>
    </ul>
  </main>
</body>
</html>
```